Infographic for a Life Transformation brand to showcase their principle method

I need a clean infographic which would be used in a brochure to show the 5 steps to achieving a Inner Uprising. (ie Life transformation). I use the theme of a revolution so I would like the graphic to include a raised fist or something to represent a revolution and then the 5 points of information to represent each step.
Needs to very clean and simple. I don't want something that would take up a full page, I want it as a graphic, almost like a big logo. I don't want it laid out like a process chart.

My brand personalities from https://markcharacterhub.com.au/ are
The Everyman and The Magician to give you an idea of my brand.

I've attached my logo so that you can see the colour of it. Graphic doesn't need to match logo but should align with that colour.

Target Market(s)

Top Tier Executives, males, 35-55y old

Industry/Entity Type

Life Coaching

Requirements
Must have
• The graphic must have the 5 Steps: in this order
1.Clarity
2. Measurement
3. Discipline
4. Nutrition
5.Exercise
Nice to have
• It could include these action steps which line up with the 5 steps, It may be too much information by there is the option to include if it works.
1.see it
2. track it
3. do it
4. eat it
5. move it

```html
<!DOCTYPE html>
<html lang="en">
<head>
<meta charset="UTF-8">
<title>5 Steps to Achieving an Inner Uprising</title>
<link href="https://fonts.googleapis.com/css2?family=Montserrat:wght@300;400;700;800&display=swap" rel="stylesheet">
<style>
  :root {
    --ink-dark: #1c1d21;
    --navy-deep: #0c1c33;
    --navy: #123a6c;
    --navy-soft: #1f4d86;
    --white: #ffffff;
    --icon-ink: #111a2a;
  }
  * { margin: 0; padding: 0; box-sizing: border-box; }
  html, body { width: 1200px; height: 1200px; overflow: hidden; }
  body {
    font-family: "Montserrat", Arial, sans-serif;
    color: var(--white);
    background: var(--ink-dark);
  }
  .infographic {
    position: relative;
    width: 1200px;
    height: 1200px;
    overflow: hidden;
    background:
      linear-gradient(35deg, var(--ink-dark) 0%, #161c28 30%, var(--navy-deep) 58%, var(--navy) 100%);
  }
  .portrait-area {
    position: absolute;
    right: 0;
    top: 40px;
    width: 620px;
    height: 1160px;
    background:
      radial-gradient(ellipse 46% 36% at 58% 38%, rgba(49,95,156,0.55) 0%, rgba(31,77,134,0.25) 55%, rgba(18,58,108,0) 100%),
      radial-gradient(ellipse 60% 45% at 60% 85%, rgba(44,82,135,0.45) 0%, rgba(18,58,108,0) 100%);
  }
  .headline {
    position: absolute;
    left: 60px;
    top: 86px;
    font-weight: 800;
    font-size: 55px;
    line-height: 59px;
    letter-spacing: -0.5px;
    text-transform: uppercase;
  }
  .step { position: absolute; left: 0; width: 1000px; height: 200px; }
  .step-number {
    position: absolute;
    top: 0;
    height: 200px;
    line-height: 200px;
    font-weight: 800;
    font-size: 48px;
  }
  .step-badge { position: absolute; top: 0; width: 180px; height: 200px; }
  .step-connector { position: absolute; top: 90px; width: 46px; height: 20px; }
  .step-text { position: absolute; top: 57px; text-align: center; }
  .step-title {
    font-weight: 800;
    font-size: 57px;
    line-height: 58px;
    letter-spacing: 1px;
    text-transform: uppercase;
  }
  .step-action {
    margin-top: 8px;
    font-weight: 300;
    font-size: 32px;
    line-height: 36px;
    letter-spacing: 5px;
    text-transform: uppercase;
  }
  .step--odd .step-number { left: 170px; }
  .step--odd .step-badge { left: 238px; }
  .step--odd .step-connector { left: 419px; }
  .step--odd .step-text { left: 495px; }
  .step--even .step-number { left: 60px; }
  .step--even .step-badge { left: 114px; }
  .step--even .step-connector { left: 292px; }
  .step--even .step-text { left: 362px; }
  .brand-name {
    position: absolute;
    left: 1123px;
    top: 810px;
    transform: translate(-50%, -50%) rotate(-90deg);
    white-space: nowrap;
    font-weight: 400;
    font-size: 34px;
    letter-spacing: 9px;
    text-transform: uppercase;
  }
</style>
</head>
<body>
<main class="infographic">
  <div class="portrait-area" role="img" aria-label="Portrait photograph of the coach, tinted in navy blue"></div>

  <h1 class="headline">5 Steps to Achieving<br>an Inner Uprising</h1>

  <svg width="0" height="0" style="position:absolute">
    <defs>
      <g id="hex-frame">
        <polygon points="90,4 172,52 172,148 90,196 8,148 8,52" fill="none" stroke="#ffffff" stroke-width="5" stroke-linejoin="round"/>
        <polygon points="90,20 158,60 158,140 90,180 22,140 22,60" fill="#ffffff"/>
      </g>
      <path id="connector-line" d="M0 10 H46" stroke="#ffffff" stroke-width="4" fill="none"/>
    </defs>
  </svg>

  <section class="step step--odd" style="top:240px">
    <span class="step-number">1</span>
    <svg class="step-badge" viewBox="0 0 180 200" aria-hidden="true">
      <use href="#hex-frame"/>
      <circle cx="90" cy="94" r="38" fill="none" stroke="var(--icon-ink)" stroke-width="7"/>
      <polygon points="78,128 102,128 90,142" fill="var(--icon-ink)"/>
      <path d="M64 96 Q90 72 116 96 Q90 116 64 96 Z" fill="none" stroke="var(--icon-ink)" stroke-width="5"/>
      <path d="M66 84 Q90 68 116 84" fill="none" stroke="var(--icon-ink)" stroke-width="4"/>
      <circle cx="88" cy="96" r="8" fill="var(--icon-ink)"/>
    </svg>
    <svg class="step-connector" viewBox="0 0 46 20" aria-hidden="true"><use href="#connector-line"/></svg>
    <div class="step-text">
      <h2 class="step-title">Clarity</h2>
      <p class="step-action">(See it)</p>
    </div>
  </section>

  <section class="step step--even" style="top:414px">
    <span class="step-number">2</span>
    <svg class="step-badge" viewBox="0 0 180 200" aria-hidden="true">
      <use href="#hex-frame"/>
      <path d="M48 68 V84 M132 68 V84 M50 76 H130" stroke="var(--icon-ink)" stroke-width="3" fill="none"/>
      <path d="M56 71 L50 76 L56 81 M124 71 L130 76 L124 81" stroke="var(--icon-ink)" stroke-width="3" fill="none"/>
      <rect x="48" y="92" width="84" height="38" fill="none" stroke="var(--icon-ink)" stroke-width="5"/>
      <path d="M58 94 V108 M66 94 V104 M74 94 V108 M82 94 V104 M90 94 V112 M98 94 V104 M106 94 V108 M114 94 V104 M122 94 V108" stroke="var(--icon-ink)" stroke-width="3"/>
    </svg>
    <svg class="step-connector" viewBox="0 0 46 20" aria-hidden="true"><use href="#connector-line"/></svg>
    <div class="step-text">
      <h2 class="step-title">Measurement</h2>
      <p class="step-action">(Track it)</p>
    </div>
  </section>

  <section class="step step--odd" style="top:577px">
    <span class="step-number">3</span>
    <svg class="step-badge" viewBox="0 0 180 200" aria-hidden="true">
      <use href="#hex-frame"/>
      <rect x="60" y="64" width="60" height="80" rx="6" fill="none" stroke="var(--icon-ink)" stroke-width="6"/>
      <rect x="76" y="54" width="28" height="16" rx="3" fill="var(--icon-ink)"/>
      <path d="M72 90 H108 M72 106 H108 M72 122 H108" stroke="var(--icon-ink)" stroke-width="5"/>
    </svg>
    <svg class="step-connector" viewBox="0 0 46 20" aria-hidden="true"><use href="#connector-line"/></svg>
    <div class="step-text">
      <h2 class="step-title">Discipline</h2>
      <p class="step-action">(Do it)</p>
    </div>
  </section>

  <section class="step step--even" style="top:749px">
    <span class="step-number">4</span>
    <svg class="step-badge" viewBox="0 0 180 200" aria-hidden="true">
      <use href="#hex-frame"/>
      <path d="M90 138 L58 106 Q44 90 56 74 Q72 58 90 78 Q108 58 124 74 Q136 90 122 106 L104 124" fill="none" stroke="var(--icon-ink)" stroke-width="6" stroke-linejoin="round"/>
      <circle cx="80" cy="124" r="10" fill="none" stroke="var(--icon-ink)" stroke-width="5"/>
      <circle cx="112" cy="118" r="5" fill="var(--icon-ink)"/>
      <path d="M84 102 Q94 102 96 112 M80 92 Q104 92 106 114" stroke="var(--icon-ink)" stroke-width="4" fill="none"/>
    </svg>
    <svg class="step-connector" viewBox="0 0 46 20" aria-hidden="true"><use href="#connector-line"/></svg>
    <div class="step-text">
      <h2 class="step-title">Nutrition</h2>
      <p class="step-action">(Eat it)</p>
    </div>
  </section>

  <section class="step step--odd" style="top:924px">
    <span class="step-number">5</span>
    <svg class="step-badge" viewBox="0 0 180 200" aria-hidden="true">
      <use href="#hex-frame"/>
      <rect x="48" y="124" width="84" height="10" rx="5" fill="var(--icon-ink)"/>
      <path d="M58 134 V142 M120 134 V142" stroke="var(--icon-ink)" stroke-width="6"/>
      <path d="M126 126 L132 76 M124 70 L134 82" stroke="var(--icon-ink)" stroke-width="5" fill="none"/>
      <path d="M64 86 H96 M70 98 H104 M76 110 H110" stroke="var(--icon-ink)" stroke-width="5" stroke-linecap="round"/>
    </svg>
    <svg class="step-connector" viewBox="0 0 46 20" aria-hidden="true"><use href="#connector-line"/></svg>
    <div class="step-text">
      <h2 class="step-title">Exercise</h2>
      <p class="step-action">(Move it)</p>
    </div>
  </section>

  <p class="brand-name">Inner Uprising</p>
</main>
</body>
</html>
```